Hello , we need a 1 page A4 flyer. the flyer needs a heading and then 4 sub headings and catagoring. The words on the attached example are the same length as our text. we are open to a new modern look and the information can be in 1 or 2 coloums. we are an australian law firm and I have also attachd our logo. the bottom 1/4 of the page is a graphic you need to allow space for. we have blue as a corporate colour and do not have a font or style. please use the 5 headings and we will complete the words / text afterwards so we will need the final version to be a word document. for assistance see www.juristcove.com.au
Industry/Entity Type
Legal
Look and feel

```html
<!DOCTYPE html>
<html lang="en">
<head>
<meta charset="utf-8">
<title>JuristCove Flyer</title>
<link href="https://fonts.googleapis.com/css2?family=Jost:wght@400;500;700&family=Fira+Sans:wght@600&display=swap" rel="stylesheet">
<style>
  :root {
    --navy: #2e3192;
    --cyan: #00a6d8;
    --brand-blue: #1b75bc;
    --icon-blue: #1b9ad6;
    --ink: #3a3a44;
    --page-top: #ffffff;
    --page-bottom: #d9d9ea;
    --canvas: #ffffff;
  }
  * { margin: 0; padding: 0; box-sizing: border-box; }
  html, body { width: 1200px; height: 1200px; overflow: hidden; background: var(--canvas); }
  .flyer {
    position: absolute; left: 176px; top: 0; width: 848px; height: 1200px;
    background: linear-gradient(180deg, var(--page-top) 15%, var(--page-bottom) 100%);
    font-family: "Jost", sans-serif; color: var(--ink); overflow: hidden;
  }
  .masthead {
    position: absolute; left: 0; top: 0; width: 848px; height: 159px;
    background: linear-gradient(90deg, #ffffff 0%, #ffffff 27%, var(--cyan) 58%, var(--cyan) 100%);
  }
  .brand-name {
    position: absolute; left: 69px; top: 84px;
    font-weight: 500; font-size: 33px; line-height: 40px; color: var(--brand-blue);
  }
  .brand-tagline {
    position: absolute; left: 69px; top: 126px;
    font-weight: 500; font-size: 12.5px; color: var(--brand-blue); letter-spacing: 0.4px;
  }
  .contact {
    position: absolute; left: 520px; top: 32px; color: #fff; font-size: 13px; line-height: 17px;
  }
  .contact p + p { margin-top: 17px; }
  .title {
    position: absolute; left: 0; width: 848px; top: 176px; text-align: center;
    font-weight: 700; font-size: 33px; color: var(--navy);
  }
  .intro {
    position: absolute; left: 20px; width: 808px; top: 219px; text-align: center;
    font-size: 14.6px; line-height: 23px; font-weight: 500; color: #333; white-space: nowrap;
  }
  .section-head { position: absolute; left: 50px; height: 38px; }
  .section-head .bar {
    position: absolute; left: 20px; top: 0; height: 37px; background: var(--navy);
    border-radius: 0 19px 19px 0; color: #fff;
    font-family: "Fira Sans", sans-serif; font-weight: 600; font-size: 18.5px;
    line-height: 37px; padding-left: 32px; padding-right: 24px; white-space: nowrap;
  }
  .section-head .badge {
    position: absolute; left: -1px; top: -5px; width: 47px; height: 47px; border-radius: 50%;
    background: #fff; border: 3px solid var(--navy); display: flex; align-items: center; justify-content: center;
  }
  .copy {
    position: absolute; left: 99px; width: 672px; font-size: 13.4px; line-height: 19.8px; color: var(--ink);
  }
  .copy p + p { margin-top: 20px; }
  .feature-photo {
    position: absolute; left: 0; top: 966px; width: 848px; height: 234px;
    background: linear-gradient(180deg, #dcdcea 0%, #eef0f4 30%, #e6ecf2 70%, #cfdde8 100%);
  }
</style>
</head>
<body>
<div class="flyer">
  <header class="masthead">
    <div class="brand-name">JuristCove</div>
    <div class="brand-tagline">practical legal support</div>
    <div class="contact">
      <p>JuristCove<br>Level 12, 40 Harbour Row Sydney NSW 2000<br>DX 318 Sydney</p>
      <p>Phone: 02 9000 1234&nbsp; Fax: 02 9000 5678<br>Email: enquiries@juristcove.com.au</p>
    </div>
  </header>

  <h1 class="title">Who is JuristCove?</h1>
  <p class="intro">This is a statement header small paragraph. This is a statement header small paragraph. This is a state-<br>ment header small paragraph. This is a statement header small paragraph</p>

  <div class="section-head" style="top:287px">
    <div class="bar" style="width:532px">Next generation legal and lender process services</div>
    <div class="badge">
      <svg width="26" height="26" viewBox="0 0 26 26" fill="none" stroke="var(--icon-blue)" stroke-width="1.4"><circle cx="9" cy="7" r="4"/><path d="M2 22c0-5 3-8 7-8s7 3 7 8"/><rect x="15" y="12" width="9" height="11"/><path d="M17 15h5M17 18h5M17 21h3"/></svg>
    </div>
  </div>
  <div class="copy" style="top:328px">
    <p>Paragraph&nbsp;1. Paragraph&nbsp;1. Paragraph&nbsp;1. Paragraph&nbsp;1. Paragraph&nbsp;1. Paragraph&nbsp;1. Paragraph&nbsp;1. Paragraph&nbsp;1. Paragraph&nbsp;1. Paragraph&nbsp;1. Paragraph&nbsp;1. Paragraph&nbsp;1. Paragraph&nbsp;1. Paragraph&nbsp;1. Paragraph&nbsp;1. Paragraph&nbsp;1.</p>
    <p>Paragraph&nbsp;2. Paragraph&nbsp;2. Paragraph&nbsp;2. Paragraph&nbsp;2. Paragraph&nbsp;2. Paragraph&nbsp;2. Paragraph&nbsp;2. Paragraph&nbsp;2. Paragraph&nbsp;2. Paragraph&nbsp;2. Paragraph&nbsp;2. Paragraph&nbsp;2. Paragraph&nbsp;2. Paragraph&nbsp;2. Paragraph&nbsp;2. Paragraph&nbsp;2. Paragraph&nbsp;2. Paragraph&nbsp;2. Paragraph&nbsp;2.</p>
  </div>

  <div class="section-head" style="top:464px">
    <div class="bar" style="width:323px">How you will benefit from us</div>
    <div class="badge">
      <svg width="26" height="26" viewBox="0 0 26 26" fill="none" stroke="var(--icon-blue)" stroke-width="1.4"><path d="M3 23h20"/><rect x="4" y="16" width="3" height="7"/><rect x="9" y="13" width="3" height="10"/><rect x="14" y="10" width="3" height="13"/><rect x="19" y="7" width="3" height="16"/><path d="M4 12l6-5 4 3 8-7M18 3h4v4"/></svg>
    </div>
  </div>
  <div class="copy" style="top:507px">
    <p>Paragraph&nbsp;1. Paragraph&nbsp;1. Paragraph&nbsp;1. Paragraph&nbsp;1. Paragraph&nbsp;1. Paragraph&nbsp;1. Paragraph&nbsp;1. Paragraph&nbsp;1. Paragraph&nbsp;1. Paragraph&nbsp;1. Paragraph&nbsp;1. Paragraph&nbsp;1. Paragraph&nbsp;1. Paragraph&nbsp;1. Paragraph&nbsp;1. Paragraph&nbsp;1. Paragraph&nbsp;1. Paragraph&nbsp;1. Paragraph&nbsp;1. Paragraph&nbsp;1. Paragraph&nbsp;1. Paragraph&nbsp;1. Paragraph&nbsp;1. Paragraph&nbsp;1. Paragraph&nbsp;1. Paragraph&nbsp;1. Paragraph&nbsp;1. Paragraph&nbsp;1. Paragraph&nbsp;1. Paragraph&nbsp;1. Paragraph&nbsp;1. Paragraph&nbsp;1. Paragraph&nbsp;1. Paragraph&nbsp;1.</p>
  </div>

  <div class="section-head" style="top:624px">
    <div class="bar" style="width:585px">We understand the Importance of the work we do for you</div>
    <div class="badge">
      <svg width="26" height="26" viewBox="0 0 26 26" fill="none" stroke="var(--icon-blue)" stroke-width="1.4"><path d="M8 3h11l4 4v16H8z"/><path d="M11 11h9M11 14h9M11 17h9M11 20h6"/><circle cx="6" cy="7" r="4" fill="#fff"/><path d="M4.5 7l1.2 1.2L8 5.8"/></svg>
    </div>
  </div>
  <div class="copy" style="top:667px">
    <p>Paragraph&nbsp;1. Paragraph&nbsp;1. Paragraph&nbsp;1. Paragraph&nbsp;1. Paragraph&nbsp;1. Paragraph&nbsp;1. Paragraph&nbsp;1. Paragraph&nbsp;1. Paragraph&nbsp;1. Paragraph&nbsp;1. Paragraph&nbsp;1. Paragraph&nbsp;1. Paragraph&nbsp;1. Paragraph&nbsp;1. Paragraph&nbsp;1. Paragraph&nbsp;1. Paragraph&nbsp;1. Paragraph&nbsp;1.</p>
    <p>Paragraph&nbsp;2. Paragraph&nbsp;2. Paragraph&nbsp;2. Paragraph&nbsp;2. Paragraph&nbsp;2. Paragraph&nbsp;2. Paragraph&nbsp;2. Paragraph&nbsp;2. Paragraph&nbsp;2. Paragraph&nbsp;2. Paragraph&nbsp;2. Paragraph&nbsp;2.</p>
  </div>

  <div class="section-head" style="top:805px">
    <div class="bar" style="width:323px">Results, not just promises</div>
    <div class="badge">
      <svg width="26" height="26" viewBox="0 0 26 26" fill="none" stroke="var(--icon-blue)" stroke-width="1.4"><rect x="5" y="3" width="16" height="20"/><path d="M8 8l1.5 1.5L12 7M8 14l1.5 1.5L12 13M8 19h2M14 8h4M14 14h4M13 19h5"/></svg>
    </div>
  </div>
  <div class="copy" style="top:849px">
    <p>Paragraph&nbsp;1. Paragraph&nbsp;1. Paragraph&nbsp;1. Paragraph&nbsp;1. Paragraph&nbsp;1. Paragraph&nbsp;1. Paragraph&nbsp;1. Paragraph&nbsp;1. Paragraph&nbsp;1. Paragraph&nbsp;1. Paragraph&nbsp;1</p>
    <p>Paragraph&nbsp;2. Paragraph&nbsp;2. Paragraph&nbsp;2. Paragraph&nbsp;2. Paragraph&nbsp;2. Paragraph&nbsp;2. Paragraph&nbsp;2. Paragraph&nbsp;2.</p>
  </div>

  <div class="feature-photo" role="img" aria-label="Photograph of a signed contract with a pen on a blue clipboard beside a small model house on a white desk"></div>
</div>
</body>
</html>
```